Real Estate Agent Announcement

I need an announcement postcard designed with imagery almost exactly similar to below; one side imagery and copy on the other. Palette is either desired in neutrals: off white, warm white, or very soft grey. I'd like to stick as close to example below in feeling of image evoking opulence and text to be clean and elegant. need double sided card with simple logo on the back. copy of logo attached. editable file type.

Target Market(s)

Luxury real estate market northern california

Industry/Entity Type

Real Estate

Font styles to use
Serif

```html
<!DOCTYPE html>
<html lang="en">
<head>
<meta charset="utf-8">
<title>Affiliation Announcement Postcard</title>
<link href="https://fonts.googleapis.com/css2?family=Cinzel:wght@400;600&family=Josefin+Sans:wght@300;400&display=swap" rel="stylesheet">
<style>
  :root {
    --backdrop: #9a9a9a;
    --card-black: #151515;
    --panel-top: #2a2a2a;
    --panel-bottom: #0e0e0e;
    --gold: #f2e03a;
    --gold-deep: #d9c51c;
    --text-light: #d8d8d8;
    --text-dark: #1a1a1a;
    --divider: #f4f4f4;
  }
  * { box-sizing: border-box; margin: 0; padding: 0; }
  html, body { width: 1200px; height: 1000px; overflow: hidden; }
  body {
    background: var(--backdrop);
    position: relative;
    font-family: "Josefin Sans", sans-serif;
  }
  .card {
    position: absolute;
    width: 660px;
    height: 450px;
    box-shadow: 0 6px 18px rgba(0,0,0,0.35);
    overflow: hidden;
  }
  /* Front side */
  .card-front { left: 500px; top: 40px; background: var(--card-black); display: flex; }
  .interior-photo {
    width: 470px;
    height: 100%;
    background:
      radial-gradient(ellipse at 18% 30%, #f3d8a8 0%, rgba(243,216,168,0) 30%),
      radial-gradient(ellipse at 60% 75%, #c89a6c 0%, rgba(200,154,108,0) 45%),
      linear-gradient(160deg, #7a4a2c 0%, #4b2a1a 45%, #2a1710 100%);
  }
  .panel {
    position: relative;
    flex: 1;
    border-left: 4px solid var(--divider);
    background: linear-gradient(180deg, var(--panel-top), var(--panel-bottom));
    display: flex;
    flex-direction: column;
    align-items: center;
    text-align: center;
    padding-top: 40px;
  }
  .panel-brand {
    font-family: "Cinzel", serif;
    font-weight: 400;
    font-size: 13px;
    letter-spacing: 0.5px;
    color: var(--text-light);
    padding-bottom: 6px;
    border-bottom: 1px solid var(--text-light);
  }
  .agent-name {
    margin-top: 44px;
    font-family: "Cinzel", serif;
    font-weight: 600;
    font-size: 19px;
    letter-spacing: 1px;
    color: var(--gold);
  }
  .announcement {
    margin-top: 22px;
    font-weight: 300;
    font-size: 13px;
    line-height: 1.35;
    color: var(--text-light);
  }
  .announcement .firm { display: block; font-weight: 400; text-transform: uppercase; font-size: 12.5px; }
  .service {
    margin-top: 34px;
    font-weight: 300;
    font-size: 13px;
    color: var(--text-light);
    line-height: 1.3;
  }
  .service .headline {
    display: block;
    font-family: "Cinzel", serif;
    font-weight: 600;
    font-size: 16px;
    color: var(--gold);
  }
  .address-band {
    position: absolute;
    left: 0; right: 0;
    bottom: 24px;
    height: 68px;
    background: linear-gradient(180deg, var(--gold) 0%, var(--gold-deep) 100%);
    display: flex;
    flex-direction: column;
    justify-content: center;
    font-size: 14px;
    line-height: 1.35;
    color: var(--text-dark);
  }
  /* Back side */
  .card-back {
    left: 40px; top: 510px;
    background: radial-gradient(ellipse at 40% 45%, #2a2a2a 0%, var(--card-black) 70%);
  }
  .back-brand {
    position: absolute;
    left: 0;
    width: 520px;
    top: 190px;
    text-align: center;
    font-family: "Cinzel", serif;
    font-weight: 600;
    font-size: 40px;
    line-height: 1.15;
    color: var(--gold);
  }
</style>
</head>
<body>
  <section class="card card-front">
    <div class="interior-photo" role="img" aria-label="Photograph of an opulent candlelit sitting room with antique chairs, side table, bookcase and rug"></div>
    <div class="panel">
      <div class="panel-brand">The Mara Lind Group</div>
      <div class="agent-name">ELENA MARSH</div>
      <p class="announcement">Is Pleased to Announce<br>Her Affiliation With<span class="firm">Harbor Oak Realty</span></p>
      <p class="service">For All of your<span class="headline">REAL ESTATE NEED</span></p>
      <div class="address-band">
        <span>418 Alder Crest Ste. 300</span>
        <span>Larkspur, CA. 94939</span>
      </div>
    </div>
  </section>

  <section class="card card-back">
    <div class="back-brand">The Mara Lind<br>Group</div>
  </section>
</body>
</html>
```